Fenwell Building Partners Stationary Revamp

We need a full set of new stationary including business cards for our Public Sector Construction company based in the South East of England. We have a new logo (attached) that we want to launch and revamp all of our company literature. We are required to send a lot of correspondence to residents etc so a consistent theme is required across everything. Also attached is our existing templates.

Target Market(s)

We work for Council and government provided housing organisations and NOT private individuals. All of our clients represent government spent money, so we need to look professional and instantly recognisable brand.

Industry/Entity Type

Business

Colors

Designer to choose colors to be used in the design.

Requirements
Must have
• New fresh designs that utilise our new logo. And the letterhead needs to be able to be rolled out onto a word template so that all staff can type straight onto it rather than us having to have it printed first.
Nice to have
• I am looking forward to seeing your best efforts as designers.

```html
<!DOCTYPE html>
<html lang="en">
<head>
<meta charset="utf-8">
<title>Fenwell Building Partners – Stationery</title>
<link href="https://fonts.googleapis.com/css2?family=Open+Sans:wght@400;600;700&display=swap" rel="stylesheet">
<style>
  :root {
    --backdrop: #e6e7e8;
    --paper: #ffffff;
    --ink: #0a0a0a;
    --gold: #c9982c;
    --gold-light: #f0c419;
    --text-light: #ffffff;
    --shadow: rgba(0,0,0,0.35);
  }
  html, body {
    margin: 0; padding: 0;
    width: 1200px; height: 927px;
    overflow: hidden;
    background: var(--backdrop);
    font-family: "Open Sans", sans-serif;
  }
  .stationery { position: relative; width: 1200px; height: 927px; }
  .letterhead, .card {
    position: absolute;
    background: var(--paper);
    overflow: hidden;
    box-shadow: 8px 10px 14px var(--shadow);
  }
  .letterhead { left: 66px; top: 53px; width: 635px; height: 821px; }
  .card { left: 753px; width: 381px; height: 218px; border-radius: 18px; }
  .card-front { top: 230px; }
  .card-back { top: 479px; }
  .artwork { position: absolute; inset: 0; width: 100%; height: 100%; }
  .brand-name { font-family: "Open Sans", sans-serif; font-weight: 700; fill: var(--ink); }
  .brand-dot { fill: var(--gold); }
  .footer-text { font-family: "Open Sans", sans-serif; fill: var(--text-light); }
  .divider { stroke: var(--gold); stroke-width: 1; }
  .icon { fill: none; stroke: var(--gold); stroke-width: 1.2; }
  .person-name { font-family: "Open Sans", sans-serif; font-weight: 700; fill: var(--gold); }
  .person-title { font-family: "Open Sans", sans-serif; fill: var(--ink); }
</style>
</head>
<body>
<main class="stationery">

  <!-- Letterhead -->
  <section class="letterhead">
    <svg class="artwork" viewBox="0 0 794 1026" preserveAspectRatio="none">
      <defs>
        <linearGradient id="goldSweep" x1="0" y1="0" x2="1" y2="0">
          <stop offset="0" stop-color="#a87a24"/>
          <stop offset="0.45" stop-color="#f0c419"/>
          <stop offset="0.55" stop-color="#f2d060"/>
          <stop offset="0.75" stop-color="#e8b817"/>
          <stop offset="1" stop-color="#b98828"/>
        </linearGradient>
      </defs>
      <g class="brand">
        <circle class="brand-dot" cx="38" cy="112" r="9"/>
        <text class="brand-name" x="54" y="119" font-size="20">Fenwell Building Partners</text>
      </g>
      <path d="M0,960 Q430,700 794,924 L794,1026 L0,1026 Z" fill="url(#goldSweep)"/>
      <path d="M0,966 Q440,760 794,1020 L794,1026 L0,1026 Z" fill="var(--ink)" stroke="#ffffff" stroke-width="2"/>
      <g class="footer-text" font-size="16" text-anchor="end">
        <text x="341" y="935">Harlow House,</text>
        <text x="341" y="955">12 Brookmead Road</text>
        <text x="341" y="974">Ashford, Kent, TN23 4QD</text>
      </g>
      <line class="divider" x1="373" y1="902" x2="373" y2="996"/>
      <g class="icon">
        <rect x="404" y="903" width="7" height="11" rx="1"/>
        <path d="M402,930 h12 v-3 a6,4 0 0 0 -12,0 Z"/>
        <path d="M405,942 q-2,6 5,11"/>
        <rect x="402" y="963" width="12" height="8"/><path d="M402,963 l6,5 l6,-5"/>
        <circle cx="408" cy="987" r="6"/><path d="M402,987 h12 M408,981 v12"/>
      </g>
      <g class="footer-text" font-size="16">
        <text x="425" y="915">+44 (0)7700 900123</text>
        <text x="425" y="935">+44 (0)20 7946 0370</text>
        <text x="425" y="954">+44  (0)20 7946 0377</text>
        <text x="425" y="974">martin.hale@fenwellbp.co.uk</text>
        <text x="425" y="994">www.fenwellbp.co.uk</text>
      </g>
    </svg>
  </section>

  <!-- Business card front -->
  <section class="card card-front">
    <svg class="artwork" viewBox="0 0 477 272" preserveAspectRatio="none">
      <defs>
        <linearGradient id="goldSweepCard" x1="0" y1="0" x2="1" y2="0">
          <stop offset="0" stop-color="#a87a24"/>
          <stop offset="0.5" stop-color="#f0c419"/>
          <stop offset="0.6" stop-color="#f2d060"/>
          <stop offset="1" stop-color="#b98828"/>
        </linearGradient>
      </defs>
      <g class="brand">
        <circle class="brand-dot" cx="30" cy="88" r="7"/>
        <text class="brand-name" x="43" y="94" font-size="15">Fenwell Building Partners</text>
      </g>
      <text class="person-name" x="451" y="38" font-size="21" text-anchor="end">Martin Hale</text>
      <text class="person-title" x="451" y="55" font-size="12" text-anchor="end">Managing Director</text>
      <path d="M0,200 Q290,40 477,180 L477,272 L0,272 Z" fill="url(#goldSweepCard)"/>
      <path d="M0,204 Q300,80 477,236 L477,272 L0,272 Z" fill="var(--ink)" stroke="#ffffff" stroke-width="1.5"/>
      <g class="footer-text" font-size="12" text-anchor="end">
        <text x="184" y="202">Harlow House,</text>
        <text x="184" y="217">12 Brookmead Road</text>
        <text x="184" y="232">Ashford, Kent, TN23 4QD</text>
      </g>
      <line class="divider" x1="209" y1="177" x2="209" y2="250"/>
      <g class="icon" stroke-width="1">
        <rect x="232" y="178" width="5" height="8" rx="1"/>
        <path d="M230,199 h9 v-2 a4.5,3 0 0 0 -9,0 Z"/>
        <path d="M232,208 q-1,5 4,8"/>
        <rect x="230" y="224" width="9" height="6"/><path d="M230,224 l4.5,3.5 l4.5,-3.5"/>
        <circle cx="234.5" cy="242" r="4.5"/><path d="M230,242 h9 M234.5,237.5 v9"/>
      </g>
      <g class="footer-text" font-size="12">
        <text x="248" y="187">+44 (0)7700 900123</text>
        <text x="248" y="202">+44 (0)20 7946 0370</text>
        <text x="248" y="217">+44  (0)20 7946 0377</text>
        <text x="248" y="232">martin.hale@fenwellbp.co.uk</text>
        <text x="248" y="247">www.fenwellbp.co.uk</text>
      </g>
    </svg>
  </section>

  <!-- Business card back -->
  <section class="card card-back">
    <svg class="artwork" viewBox="0 0 477 272" preserveAspectRatio="none">
      <g class="brand">
        <circle class="brand-dot" cx="92" cy="138" r="9"/>
        <text class="brand-name" x="246" y="146" font-size="22" text-anchor="middle">Fenwell Building Partners</text>
      </g>
    </svg>
  </section>

</main>
</body>
</html>
```